Partlow Law Stationery - Letterhead, Envelopes, Business Cards

We need high quality business stationery for our Personal Injury Law Firm located in Houston, Texas. The design should include the logo, Partlow Law Group, PLLC, 713-555-0148, 2750 Marlowe Crescent, Suite 318, Houston, Texas 77099 www.PartlowLaw.example. The colors are blue and white. The letterhead should also include the Attorneys - Marcy Teague, Everett K. Partlow and Dorian Fisk.

```html
<!DOCTYPE html>
<html lang="en">
<head>
<meta charset="utf-8">
<title>Partlow Law Group, PLLC – Letterhead</title>
<link href="https://fonts.googleapis.com/css2?family=Figtree:wght@400;500;700;800&display=swap" rel="stylesheet">
<style>
  :root {
    --navy: #1b2657;
    --navy-deep: #06143a;
    --band-grey: #858585;
    --ink: #2b2b2b;
    --muted: #6a6a6a;
    --paper: #ffffff;
    --backdrop: #e2e2e2;
  }
  * { box-sizing: border-box; margin: 0; padding: 0; }
  html, body { width: 1200px; height: 1200px; overflow: hidden; }
  body {
    background: var(--backdrop);
    font-family: "Figtree", sans-serif;
    color: var(--ink);
    position: relative;
  }
  .letterhead {
    position: absolute;
    left: 216px; top: 76px;
    width: 768px; height: 1046px;
    background: var(--paper);
    overflow: hidden;
  }
  .brand {
    position: absolute; left: 56px; top: 71px;
    display: flex; align-items: center; gap: 12px;
  }
  .brand-mark {
    width: 74px; height: 74px; border-radius: 50%;
    background: var(--navy);
  }
  .brand-name {
    font-weight: 800; font-size: 19px; line-height: 1.15;
    color: var(--navy); text-transform: uppercase; width: 170px;
  }
  .attorneys {
    position: absolute; left: 559px; top: 51px;
    border-left: 3px solid var(--navy);
    padding-left: 9px; height: 111px;
    display: flex; flex-direction: column; justify-content: space-between;
  }
  .attorney-name { font-weight: 700; font-size: 17px; line-height: 1; color: var(--navy); }
  .attorney-role { font-size: 12.5px; line-height: 1.1; color: var(--ink); text-transform: uppercase; margin-top: 2px; }
  .backdrop-ring {
    position: absolute; left: 98px; top: 241px;
    width: 580px; height: 580px; border-radius: 50%;
    border: 22px solid #f7f7f7;
  }
  .letter-body {
    position: absolute; left: 55px; top: 303px; width: 659px;
    font-size: 17.4px; line-height: 26px; text-align: justify;
  }
  .letter-body p + p { margin-top: 26px; }
  .letter-body p:first-child { text-indent: 18px; }
  .signoff { position: absolute; left: 563px; top: 790px; }
  .signoff-name { font-size: 10px; color: var(--muted); }
  .signoff-role { font-size: 8.5px; color: var(--muted); margin-top: 3px; }
  .signature {
    position: absolute; left: 556px; top: 826px; width: 170px; height: 72px;
    background: linear-gradient(160deg, #f4f4f4, #e9e9e9);
    border-radius: 36px;
  }
  .contact {
    position: absolute; left: 0; right: 0; top: 940px;
    text-align: center; color: var(--ink);
  }
  .contact-line {
    display: flex; justify-content: center; align-items: center; gap: 32px;
    font-size: 20px; letter-spacing: 0.5px;
  }
  .contact-item { display: flex; align-items: center; gap: 8px; }
  .contact-item svg { width: 22px; height: 22px; }
  .address { font-size: 19.5px; margin-top: 8px; letter-spacing: -0.2px; }
  .footer-bands { position: absolute; left: 0; bottom: 0; width: 768px; height: 26px; }
</style>
</head>
<body>
  <main class="letterhead">
    <div class="backdrop-ring" aria-hidden="true"></div>

    <header class="brand">
      <div class="brand-mark" aria-hidden="true"></div>
      <div class="brand-name">Partlow Law Group, PLLC</div>
    </header>

    <ul class="attorneys" style="list-style:none">
      <li><div class="attorney-name">Marcy Teague</div><div class="attorney-role">Managing Partner</div></li>
      <li><div class="attorney-name">Everett K. Partlow</div><div class="attorney-role">Associate Attorney</div></li>
      <li><div class="attorney-name">Dorian Fisk</div><div class="attorney-role">Associate Attorney</div></li>
    </ul>

    <section class="letter-body">
      <p>Lorem ipsum dolor sit amet, consectetuer adipiscing elit, sed diam nonummy nibh euismod tincidunt ut laoreet dolore magna aliquam erat volutpat. Ut wisi enim ad minim veniam, quis nostrud exerci tation ullamcorper suscipit lobortis nisl ut aliquip ex ea commodo consequat. Duis autem vel eum iriure dolor in hendrerit in vulputate velit esse molestie consequat, vel illum dolore eu feugiat nulla facilisis at vero eros et accumsan et iusto odio dignissim qui blandit praesent luptatum zzril delenit augue duis dolore te feugait nulla facilisi.</p>
      <p>Lorem ipsum dolor sit amet, cons ectetuer adipiscing elit, sed diam nonummy nibh euismod tincidunt ut laoreet dolore magna aliquam erat volutpat. Ut wisi Lorem ipsum dolor sit amet, consectetuer adipiscing elit, sed diam nonummy nibh euismod tincidunt ut laoreet dolore magna aliquam erat volutpat. Ut wisi enim ad minim veniam, quis nostrud exerci tation ullamcorper suscipit lobortis nisl ut aliquip ex ea commodo consequat. Duis autem vel eum iriure dolor in hendrerit in vulputate velit esse molestie consequat, Lorem ipsum dolor sit amet, cons ectetuer adipiscing elit, sed diam nonummy nibh euismod tincidunt ut laoreet dolore magna aliquam erat volutpat.</p>
    </section>

    <div class="signoff">
      <div class="signoff-name">John Doe</div>
      <div class="signoff-role">Office Maneger</div>
    </div>
    <div class="signature" role="img" aria-label="Handwritten signature"></div>

    <footer class="contact">
      <div class="contact-line">
        <span class="contact-item">
          <svg viewBox="0 0 24 24" aria-hidden="true"><path fill="var(--navy)" d="M6.6 10.8a15.1 15.1 0 0 0 6.6 6.6l2.2-2.2c.3-.3.7-.4 1-.2 1.1.4 2.3.6 3.6.6.6 0 1 .4 1 1V20c0 .6-.4 1-1 1A17 17 0 0 1 3 4c0-.6.4-1 1-1h3.5c.6 0 1 .4 1 1 0 1.3.2 2.5.6 3.6.1.3 0 .7-.2 1z"/></svg>
          713-555-0148
        </span>
        <span class="contact-item">
          <svg viewBox="0 0 24 24" aria-hidden="true" fill="none" stroke="var(--navy)" stroke-width="1.6"><circle cx="12" cy="12" r="10"/><ellipse cx="12" cy="12" rx="4.5" ry="10"/><path d="M2 12h20M4 6.5h16M4 17.5h16M12 2v20"/></svg>
          www.PartlowLaw.example
        </span>
      </div>
      <div class="address">2750 Marlowe Crescent, Suite 318, Houston, Texas 77099</div>
    </footer>

    <svg class="footer-bands" viewBox="0 0 768 26" aria-hidden="true">
      <polygon points="0,0 377,0 360,26 0,26" fill="var(--band-grey)"/>
      <polygon points="394,0 768,0 768,26 377,26" fill="var(--navy-deep)"/>
    </svg>
  </main>
</body>
</html>
```